Broschüre für Energieberater
Zielgruppe
Unternehmen die zu den KMU´s gehören (kleine und mittlere Unternehmen) haben die Möglichkeit eine Energieberatung über die ZEKV fördern zu lassen. Diese Beratung wird durch unsere Ingenieure durchgeführt und ist für den Kunden völlig kostenneutral. Zum einen erhält er eine 80% Förderung von der ZEKV (Zentralstelle für Kostenausgleich und Versorgung) die restlichen 20% erhält der Kunde von uns als Gutschrift. Wir finanzieren uns somit nur über die Fördergelder des Bundes. Die Vorteile des Kunden sind: Verringerung von Steuern, Einsparung von mindestens 10% an Energie ohne zusätzliche Kosten und somit weniger C0² Ausstoss, was wiederum allen zugute kommt. Somit ein hohes Maß an Umweltbewusstsein! Alle Investitionen die für die Einsparung von Energie von Vorteil sind, werden vom Bund mit bis zu 200.000 Euro gefördert. Voraussetzung eine durchgeführte ZEKV Energieberatung. Somit eine win/win Situation für alle Beteiligten.
Aufgabenstellung
Das Design kann - muss - nicht an unsere Webseite : www.wattlinde-beratung.de angelehnt sein.

```html
<!DOCTYPE html>
<html lang="de">
<head>
<meta charset="utf-8">
<title>Wattlinde Beratung – Flyer</title>
<link href="https://fonts.googleapis.com/css2?family=Barlow:ital,wght@0,400;0,500;0,600;0,700;1,500;1,700&display=swap" rel="stylesheet">
<style>
  :root{
    --bg:#6fa9bd;
    --paper:#f1f0ea;
    --ink:#4a4a4a;
    --dark:#4d4d4d;
    --yellow:#e2d812;
    --blue:#5db8df;
    --card1:#3b93b3;
    --card2:#5d9fbb;
    --card3:#82b3c8;
    --card4:#5ab4dc;
    --white:#ffffff;
  }
  *{box-sizing:border-box;margin:0;padding:0}
  html,body{width:857px;height:1200px;overflow:hidden}
  body{background:var(--bg);font-family:"Barlow",sans-serif;color:var(--ink);position:relative}

  .flyer{position:absolute;left:38px;width:780px;height:390px;background:var(--paper);overflow:hidden;box-shadow:0 6px 18px rgba(0,0,0,.18)}
  .flyer--front{top:120px}
  .flyer--back{top:640px}

  /* front */
  .headline{position:absolute;left:52px;top:24px;font-weight:500;font-size:58px;line-height:56px;color:var(--ink);letter-spacing:-.5px}
  .headline .line{display:block}
  .headline .accent-row{display:block;position:relative;height:72px;margin:4px 0 2px}
  .accent-band{position:absolute;left:-52px;top:8px;width:110px;height:56px;background:var(--yellow)}
  .accent-box{position:absolute;left:0;top:0;height:72px;padding:0 20px;background:var(--yellow);border-radius:12px;color:var(--blue);font-weight:700;font-size:70px;line-height:72px;letter-spacing:1px}
  .rays{position:absolute;left:262px;top:-26px}
  .bulb-art{position:absolute;left:470px;top:20px;width:200px;height:310px;border-radius:50% 50% 12px 12px / 35% 35% 12px 12px;background:radial-gradient(circle at 50% 28%,#f3d51f 0,#f0d23a 26%,rgba(241,240,234,0) 46%),linear-gradient(var(--paper),var(--paper))}
  .tagline-band{position:absolute;left:0;bottom:0;width:610px;height:44px;background:var(--dark);color:var(--white);font-size:15px;font-weight:500;line-height:44px;padding-left:54px}
  .brand{position:absolute;display:flex;align-items:center;gap:7px;color:var(--ink);font-weight:600}
  .brand .dot{width:12px;height:12px;border-radius:50%;background:var(--blue)}
  .brand .name{font-size:26px;line-height:1}
  .brand .sub{display:block;font-size:13px;font-weight:600;margin-top:2px}
  .flyer--front .brand{right:28px;bottom:36px}

  /* back */
  .flyer--back .brand{right:26px;top:20px}
  .back-yellow{position:absolute;left:0;bottom:0;width:100%;height:170px;background:var(--yellow)}
  .title-bar{position:absolute;left:0;top:30px;height:34px;width:560px;background:var(--dark);border-radius:0 17px 17px 0;padding-left:24px;color:var(--yellow);font-weight:700;font-style:italic;font-size:24px;line-height:34px}
  .intro{position:absolute;left:24px;top:70px;width:560px;font-size:13px;font-weight:500;line-height:16px;color:var(--ink)}
  .cards{position:absolute;left:24px;top:112px;display:flex;gap:12px}
  .card{width:172px;height:232px;border-radius:12px;color:var(--white);padding:12px 12px}
  .card--1{background:var(--card1)} .card--2{background:var(--card2)}
  .card--3{background:var(--card3)} .card--4{background:var(--card4)}
  .card h3{font-size:13px;font-weight:600;font-style:italic;line-height:15px;padding-bottom:6px;border-bottom:1px solid rgba(255,255,255,.8);margin-bottom:7px;min-height:37px}
  .card p{font-size:8.2px;line-height:10.4px;font-weight:500;margin-bottom:8px}
  .more-info{position:absolute;left:24px;bottom:10px;font-size:25px;font-weight:700;font-style:italic;color:var(--ink)}
</style>
</head>
<body>

<section class="flyer flyer--front">
  <div class="bulb-art" role="img" aria-label="Glühbirne aus zerknülltem gelbem Papier mit gezeichnetem Kabel und Strahlen"></div>
  <h1 class="headline">
    <span class="line">Mit uns geht</span>
    <span class="line">Euch ein</span>
    <span class="accent-row">
      <span class="accent-band"></span>
      <span class="accent-box">LICHT</span>
      <svg class="rays" width="50" height="124" viewBox="0 0 50 124" aria-hidden="true">
        <g stroke="#e2d812" stroke-width="7">
          <line x1="8" y1="40" x2="26" y2="14"/>
          <line x1="14" y1="62" x2="42" y2="62"/>
          <line x1="8" y1="84" x2="26" y2="110"/>
        </g>
      </svg>
    </span>
    <span class="line">auf!</span>
  </h1>
  <div class="tagline-band">Experten erklären Euch wie Ihr Energie und Geld spart.</div>
  <div class="brand"><span class="dot"></span><span><span class="name">Wattlinde</span><span class="sub">Beratung</span></span></div>
</section>

<section class="flyer flyer--back">
  <div class="back-yellow"></div>
  <div class="brand"><span class="dot"></span><span><span class="name">Wattlinde</span><span class="sub">Beratung</span></span></div>

  <h2 class="title-bar">Für die Umwelt und Deine Zukunft.</h2>
  <p class="intro">Erhalten Sie jetzt Ihre staatlich geförderte Energieberatung, lassen Sie sich von Anfang an von Experten begleiten und sparen Sie ab sofort Energie und damit bares Geld!</p>

  <div class="cards">
    <article class="card card--1">
      <h3>Keine versteckten Kosten!</h3>
      <p>Deutschland ist beim Erreichen seiner Klimaziele nicht auf Kurs und will deshalb mit dem Fördern von Energieberatungen mittelständische deutsche Unternehmen motivieren, energiesparende Maßnahmen zu treffen.</p>
      <p>Die darin empfohlenen Umsetzungen sind freiwillig. Zu keinem Zeitpunkt entstehen Ihnen versteckte Kosten!</p>
    </article>
    <article class="card card--2">
      <h3>Staatliche Fördermittel sichern!</h3>
      <p>Die Fördermittel sind aktuell gesichert, dies kann der Gesetzgeber jedoch jederzeit ändern.</p>
      <p>Fördermittel sollten daher genutzt werden, solange Sie zur Verfügung stehen. Die Fördermittel werden von der Zentralstelle für Kostenausgleich und Versorgung bereitgestellt.</p>
    </article>
    <article class="card card--3">
      <h3>Bis zu 25% Energie &amp; Kosten einsparen!</h3>
      <p>Viele Unternehmer wurden bisher noch nicht ausreichend über ihren Energiehaushalt aufgeklärt. Ein auf Energieberatung spezialisierter Ingenieur erkennt schnell, an welchen Ecken mit wenig Aufwand viel Energie gespart werden kann.</p>
      <p>So wird langfristig nicht nur die Umwelt, sondern auch der eigene Geldbeutel geschont.</p>
    </article>
    <article class="card card--4">
      <h3>Experten gesicherte Durchführung!</h3>
      <p>Wattlinde kann dank seiner langen Erfahrung in der Energiebranche eine problemlose Anmeldung garantieren.</p>
      <p>Alle Formulare müssen optimal ausgefüllt sein, um die Chancen auf eine maximale Förderung zu gewährleisten. Wenn die Zusage zur Förderung eintrifft, wird Wattlinde einen vom Staat zertifizierten Ingenieur zur Energieberatung vorbei schicken.</p>
    </article>
  </div>

  <p class="more-info">Weitere Infos unter: www.wattlinde-beratung.de</p>
</section>

</body>
</html>
```